Web Design job - Condo Debts Collection Business needs a Web Design

I need a site for a client, who works with condo debts collection, and ensure all revenues provided by condo fees will be always available to the building manager of condo on a specific date, regardless of defaults.
I have the visual identity (logo, slogan and colors) of the company, and some requirements on layout (kind of slider, menu options, phone number on a noble position, etc) - maybe I can do a sketch, but I like the idea of give some freedom to designer.

*** PLEASE, we have no interest in templates. We want something new***

Target Market(s)

I have two targets for this design: - Condominium's building manager. This target is looking for a solution to overdue debts on it's condo. - Residents on condominiums. This target wants to live in a better place, where their neighbors pay their condominium fees on time.

Number of Pages Required

1 page

Requirements
Must have
• - Slider with title, some short text related, a nice image (I prefer happy and/or peaceful family, people doing business, happy friends, and so on).
• - I have a special attention to menu. I'm looking for one I can have a nice effect, more elegant, charming, kind of innovative.
• - Phone number on the top (or clearly visible).
• - Member log in area or icon on the top (or clearly visible).
• - News/articles area.
• - Modern fonts, with good quality, sans-serif on areas where reading is more intensive (prefer Google web-fonts).
• - Colors specified on attached files.
Nice to have
• - Clear background color, cause it's better to read larger texts (like articles). Dark backgrounds makes reading difficult.
• - A site with effects (like shadows, lines, curves, gradients, lights) is usually pretty.
• - I pay attention on beautiful footers.
Should not have
• - Images with a lot of money (I don't sell richness, I sell tranquility, peace, harmony, safety).
• - Poor menu.

```html
<!DOCTYPE html>
<html lang="en">
<head>
<meta charset="utf-8">
<title>Condara – Cobrança Condominial</title>
<link href="https://fonts.googleapis.com/css2?family=Montserrat:wght@500;600;700;800;900&family=Roboto:wght@400;500;700&display=swap" rel="stylesheet">
<style>
:root{
  --yellow:#f6b60f;
  --yellow-soft:#fde9a8;
  --dark:#2f2f2f;
  --text:#555;
  --muted:#8a8a8a;
  --light:#f3f3f3;
  --line:#e2e2e2;
  --white:#fff;
}
*{margin:0;padding:0;box-sizing:border-box}
html,body{width:1200px;height:2960px;overflow:hidden}
body{background:var(--white);font-family:'Roboto',sans-serif;color:var(--text);position:relative}
h1,h2,h3,h4,.btn,.nav a{font-family:'Montserrat',sans-serif}
.btn{display:inline-block;background:var(--yellow);color:var(--white);font-size:13px;font-weight:700;padding:10px 30px;border-radius:20px;text-transform:uppercase;letter-spacing:.5px}

/* header */
.site-header{position:absolute;top:0;left:0;width:1200px;height:110px;background:var(--white);z-index:2;box-shadow:0 2px 6px rgba(0,0,0,.05)}
.brand-name{position:absolute;left:80px;top:34px;font-family:'Montserrat',sans-serif;font-weight:700;font-size:32px;color:var(--dark);line-height:1}
.topbar{position:absolute;right:80px;top:8px;display:flex;gap:12px;align-items:center}
.phone{background:var(--yellow);color:var(--dark);font-weight:700;font-size:14px;padding:6px 16px;display:flex;gap:8px;align-items:center}
.login{background:var(--dark);color:var(--white);font-size:12px;padding:6px 14px;border-radius:3px;display:flex;gap:6px;align-items:center}
.nav{position:absolute;right:80px;top:56px;display:flex;gap:6px}
.nav a{font-size:13px;font-weight:600;color:var(--dark);text-decoration:none;padding:8px 20px;border-radius:18px}
.nav a.active{background:var(--yellow);color:var(--white)}

/* hero */
.hero{position:absolute;top:110px;left:0;width:1200px;height:450px;background:linear-gradient(90deg,#f6f6f6 0%,#ececec 100%);overflow:hidden}
.hero-shape{position:absolute;right:-120px;top:-40px;width:720px;height:560px;border-radius:50%;background:var(--yellow-soft)}
.hero-photo{position:absolute;right:0;top:0;width:620px;height:450px;background:linear-gradient(135deg,#e9dccb 0%,#c9a68b 45%,#f4e2b4 100%);clip-path:ellipse(72% 85% at 78% 50%)}
.hero-text{position:absolute;left:80px;top:160px}
.hero-text .welcome{font-family:'Montserrat',sans-serif;font-weight:800;font-size:28px;color:var(--dark)}
.hero-text h1{font-size:72px;font-weight:900;color:var(--yellow);line-height:1;margin-top:4px}
.hero-text .sub{font-family:'Montserrat',sans-serif;font-weight:800;font-size:26px;color:var(--yellow);margin:4px 0 26px}
.dots{position:absolute;left:80px;top:408px;display:flex;gap:8px}
.dots span{width:10px;height:10px;border-radius:50%;background:#ccc}
.dots span.on{background:var(--yellow)}

/* about */
.about{position:absolute;top:640px;left:80px;width:1040px;height:320px}
.about-photo{position:absolute;left:0;top:20px;width:470px;height:250px;background:linear-gradient(180deg,#bcd9ef 0%,#e9eef2 55%,#56b8d8 100%)}
.about-body{position:absolute;left:520px;top:0;width:520px}
.section-title{font-size:34px;font-weight:700;color:var(--dark);letter-spacing:1px;line-height:1.2}
.about-body .section-title{padding-bottom:12px;border-bottom:2px solid var(--line);margin-bottom:16px}
.copy{font-size:13px;line-height:1.6;color:var(--text)}
.about-body .btn{margin-top:20px}

/* services */
.services{position:absolute;top:1020px;left:0;width:1200px;height:950px;background:var(--light)}
.services .section-title{position:absolute;top:70px;width:100%;text-align:center}
.services .underline{position:absolute;top:120px;left:80px;width:1040px;height:2px;background:var(--line)}
.service-row{position:absolute;left:80px;width:1040px;height:380px;display:flex}
.service-row.first{top:160px}
.service-row.second{top:540px}
.service-card{width:520px;height:380px;background:var(--white);padding:60px 40px;box-shadow:0 4px 14px rgba(0,0,0,.06)}
.service-card h3{font-size:17px;font-weight:800;color:var(--yellow);text-transform:uppercase;margin-bottom:16px}
.service-card .btn{margin-top:24px}
.service-photo{width:520px;height:380px}
.photo-business{background:linear-gradient(135deg,#d7d9dc 0%,#9aa3ab 50%,#e4e1dc 100%)}
.photo-family{background:linear-gradient(135deg,#d9cfc2 0%,#a89a89 50%,#e8e4df 100%)}

/* blog */
.blog{position:absolute;top:1990px;left:80px;width:1040px}
.blog .section-title{text-align:center;margin-top:30px}
.blog .underline{height:2px;background:var(--line);margin:14px 0 30px}
.posts{display:grid;grid-template-columns:500px 500px;column-gap:40px;row-gap:40px}
.post{display:flex;height:200px}
.post-photo{width:210px;height:200px}
.post-date{width:44px;height:200px;background:var(--yellow);color:var(--white);font-family:'Montserrat',sans-serif;text-align:center;padding-top:40px}
.post-date .y{font-size:11px;font-weight:600}
.post-date .d{font-size:22px;font-weight:800;margin:6px 0}
.post-date .m{font-size:12px;font-weight:600}
.post-body{padding:6px 0 0 16px;width:246px}
.post-body h4{font-size:14px;font-weight:700;color:var(--dark);line-height:1.35;margin-bottom:10px}
.post-body .copy{font-size:12px;line-height:1.5}
.read{display:block;margin-top:10px;font-size:13px;font-weight:700;color:var(--yellow)}
.ph-a{background:linear-gradient(160deg,#7aa2c4,#3c4f63)}
.ph-b{background:linear-gradient(160deg,#c6d7e5,#8e8e8e)}
.ph-c{background:linear-gradient(160deg,#2b3446,#c78b43)}
.ph-d{background:linear-gradient(160deg,#a9c9e6,#b58a5c)}
.view-more{position:absolute;top:2580px;left:0;width:1200px;text-align:center}

/* footer */
.site-footer{position:absolute;top:2645px;left:0;width:1200px;height:265px;background:#f7f7f7;border-top:1px solid var(--line)}
.footer-col{position:absolute;top:28px}
.footer-col h4{font-size:14px;font-weight:700;color:var(--dark);text-transform:uppercase;padding-bottom:10px;border-bottom:1px solid var(--line);margin-bottom:16px}
.info{left:80px;width:420px}
.info li{list-style:none;display:flex;gap:12px;font-size:12px;line-height:1.5;margin-bottom:14px;align-items:flex-start}
.info svg{flex:none;margin-top:2px}
.contact{left:500px;width:480px}
.form-grid{display:grid;grid-template-columns:1fr 1fr;column-gap:30px;row-gap:14px}
.field{font-size:11px;color:var(--muted);border-bottom:1px solid #d5d5d5;padding-bottom:6px}
.field.full{grid-column:1 / 3;height:40px}
.contact .btn{margin-top:18px;font-size:11px;padding:8px 20px;border-radius:3px}
.copyright{position:absolute;top:2910px;left:0;width:1200px;height:50px;background:var(--dark);color:#ddd;font-size:12px;text-align:center;line-height:50px}
</style>
</head>
<body>

<header class="site-header">
  <div class="brand-name">Condara</div>
  <div class="topbar">
    <div class="phone">
      <svg width="14" height="14" viewBox="0 0 24 24"><path fill="#2f2f2f" d="M6.6 10.8a15 15 0 0 0 6.6 6.6l2.2-2.2c.3-.3.7-.4 1-.2 1.1.4 2.3.6 3.6.6.6 0 1 .4 1 1V20c0 .6-.4 1-1 1A17 17 0 0 1 3 4c0-.6.4-1 1-1h3.5c.6 0 1 .4 1 1 0 1.3.2 2.5.6 3.6.1.3 0 .7-.2 1z"/></svg>
      (81) 5550.0142
    </div>
    <div class="login">
      <svg width="12" height="12" viewBox="0 0 24 24"><circle cx="12" cy="8" r="4" fill="#fff"/><path fill="#fff" d="M4 21c0-4.4 3.6-7 8-7s8 2.6 8 7z"/></svg>
      Member Login
    </div>
  </div>
  <nav class="nav">
    <a class="active">HOME</a><a>ABOUT US</a><a>BLOG</a><a>TESTIMONIAL</a><a>CONTACT US</a>
  </nav>
</header>

<section class="hero">
  <div class="hero-shape"></div>
  <div class="hero-photo" role="img" aria-label="Happy family of four smiling together at home"></div>
  <div class="hero-text">
    <div class="welcome">WELCOME TO</div>
    <h1>CONDARA</h1>
    <div class="sub">COBRANÇA CONDOMINIAL</div>
    <span class="btn">Read More</span>
  </div>
  <div class="dots"><span class="on"></span><span></span><span></span></div>
</section>

<section class="about">
  <div class="about-photo" role="img" aria-label="Modern white house with a swimming pool"></div>
  <div class="about-body">
    <h2 class="section-title">ABOUT US</h2>
    <p class="copy">Lorem Ipsum is simply dummy text of the printing and typesetting industry. Lorem Ipsum has been the industry's standard dummy text ever since the 1500s, when an unknown printer took a galley of type and scrambled it to make a type specimen book. It has survived not only five centuries. Lorem Ipsum is simply dummy text of the printing and typesetting industry. Lorem Ipsum has been the industry's standard dummy text ever since the 1500s, when an unknown printer took a galley of type and scrambled it to make a type specimen book. It has survived not only five.</p>
    <span class="btn">Read More</span>
  </div>
</section>

<section class="services">
  <h2 class="section-title">OUR SERVICES</h2>
  <div class="underline"></div>
  <div class="service-row first">
    <div class="service-card">
      <h3>Condominium's Building Manager</h3>
      <p class="copy">Lorem Ipsum is simply dummy text of the printing and typesetting industry. Lorem Ipsum has been the industry's standard dummy text ever since the 1500s, when an unknown printer took a galley of type and scrambled it. Lorem Ipsum is simply dummy text of the printing and typesetting industry. Lorem Ipsum has been the industry's standard dummy text ever since the 1500s, when an unknown printer took a galley.</p>
      <span class="btn">Read More</span>
    </div>
    <div class="service-photo photo-business" role="img" aria-label="Building manager meeting with a couple at a table"></div>
  </div>
  <div class="service-row second">
    <div class="service-photo photo-family" role="img" aria-label="Family relaxing together on a sofa"></div>
    <div class="service-card">
      <h3>Residents on Condominiums</h3>
      <p class="copy">Lorem Ipsum is simply dummy text of the printing and typesetting industry. Lorem Ipsum has been the industry's standard dummy text ever since the 1500s, when an unknown printer took a galley of type and scrambled it to make a type specimen book. Lorem Ipsum is simply dummy text of the printing and typesetting industry. Lorem Ipsum has been the industry's standard dummy text ever since the 1500s.</p>
      <span class="btn">Read More</span>
    </div>
  </div>
</section>

<section class="blog">
  <h2 class="section-title">OUR BLOG</h2>
  <div class="underline"></div>
  <div class="posts">
    <article class="post">
      <div class="post-photo ph-a" role="img" aria-label="Residential building at dusk"></div>
      <div class="post-date"><div class="y">2017</div><div class="d">26</div><div class="m">May</div></div>
      <div class="post-body"><h4>Lorem Ipsum is simply dummy text of the printing and</h4><p class="copy">Lorem Ipsum is simply dummy text of the printing and typesetting industry. Lorem Ipsum has been the industry's standard dummy text ever since the 1500s.</p><span class="read">Read More</span></div>
    </article>
    <article class="post">
      <div class="post-photo ph-b" role="img" aria-label="White modern house exterior"></div>
      <div class="post-date"><div class="y">2017</div><div class="d">22</div><div class="m">May</div></div>
      <div class="post-body"><h4>Lorem Ipsum is simply dummy text of the printing and</h4><p class="copy">Lorem Ipsum is simply dummy text of the printing and typesetting industry. Lorem Ipsum has been the industry's standard dummy text ever since the 1500s.</p><span class="read">Read More</span></div>
    </article>
    <article class="post">
      <div class="post-photo ph-c" role="img" aria-label="House with lit windows at night"></div>
      <div class="post-date"><div class="y">2017</div><div class="d">23</div><div class="m">May</div></div>
      <div class="post-body"><h4>Lorem Ipsum is simply dummy text of the printing and</h4><p class="copy">Lorem Ipsum is simply dummy text of the printing and typesetting industry. Lorem Ipsum has been the industry's standard dummy text ever since the 1500s.</p><span class="read">Read More</span></div>
    </article>
    <article class="post">
      <div class="post-photo ph-d" role="img" aria-label="Suburban home under a blue sky"></div>
      <div class="post-date"><div class="y">2017</div><div class="d">24</div><div class="m">May</div></div>
      <div class="post-body"><h4>Lorem Ipsum is simply dummy text of the printing and</h4><p class="copy">Lorem Ipsum is simply dummy text of the printing and typesetting industry. Lorem Ipsum has been the industry's standard dummy text ever since the 1500s.</p><span class="read">Read More</span></div>
    </article>
  </div>
</section>

<div class="view-more"><span class="btn">View More</span></div>

<footer class="site-footer">
  <div class="footer-col info">
    <h4>Contact Information</h4>
    <ul>
      <li><svg width="14" height="14" viewBox="0 0 24 24"><path fill="#2f2f2f" d="M6.6 10.8a15 15 0 0 0 6.6 6.6l2.2-2.2c.3-.3.7-.4 1-.2 1.1.4 2.3.6 3.6.6.6 0 1 .4 1 1V20c0 .6-.4 1-1 1A17 17 0 0 1 3 4c0-.6.4-1 1-1h3.5c.6 0 1 .4 1 1 0 1.3.2 2.5.6 3.6.1.3 0 .7-.2 1z"/></svg>(81) 5550.0142</li>
      <li><svg width="14" height="14" viewBox="0 0 24 24"><rect x="2" y="5" width="20" height="14" rx="2" fill="#2f2f2f"/><path d="M3 6l9 7 9-7" stroke="#fff" stroke-width="1.6" fill="none"/></svg>contact@condara.example</li>
      <li><svg width="14" height="14" viewBox="0 0 24 24"><path fill="#2f2f2f" d="M12 2a7 7 0 0 0-7 7c0 5 7 13 7 13s7-8 7-13a7 7 0 0 0-7-7zm0 9.5A2.5 2.5 0 1 1 12 6.5a2.5 2.5 0 0 1 0 5z"/></svg>Rua das Palmeiras, 482, Loja 12, Centro Comercial Jardim,<br>Vila Serena, Recanto MG</li>
    </ul>
  </div>
  <div class="footer-col contact">
    <h4>Contact Us</h4>
    <div class="form-grid">
      <div class="field">Name</div>
      <div class="field">Phone No</div>
      <div class="field">Email Id</div>
      <div class="field">Subject</div>
      <div class="field full">Message</div>
    </div>
    <span class="btn">Send Message</span>
  </div>
</footer>

<div class="copyright">Copyright © 2019 Condara. All Right Reserved. | Privacy Policy | Site Map</div>

</body>
</html>
```